Need Catering Menu designed - design that we want is attached

Hi,
We need a new catering menu designed for our cafe.
I have attached our coffee menu, we would like it to follow the same kind of layout.
It needs to be A4, and can be double sided.
I have attached a word doc of our catering menu, so this is what needs to be on the catering menu you produce.
Also, our contact details need to be on both sides of the menu:
Visit us instore to discuss catering options, or call 0438 672 914 or email marla@tevrostudio.com.au
I have also attached our new logo which I'd like incorporated into the menu
Target Market(s)
Doctors/Nurses
Hospital staff
University Students
Industry/Entity Type
Catering
Look and feel

```html
<!DOCTYPE html>
<html lang="en">
<head>
<meta charset="utf-8">
<title>Bedside Cafe – Catering Menu</title>
<link rel="stylesheet" href="https://fonts.googleapis.com/css2?family=Open+Sans:ital,wght@0,400;0,600;1,400&display=swap">
<style>
:root{
  --canvas:#ffffff;
  --page-edge:#3a2f2a;
  --page-top:#6a5a4d;
  --page-bottom:#4d3f36;
  --panel:#2d2430;
  --panel-line:#ffffff;
  --ink:#ffffff;
  --ink-soft:#e8e2e6;
  --peach:#f2b48a;
  --cream:#fbf1e6;
}
*{margin:0;padding:0;box-sizing:border-box}
html,body{width:800px;height:1200px;overflow:hidden;background:var(--canvas)}
body{position:relative;font-family:"Open Sans",Arial,sans-serif;color:var(--ink)}
.page{position:absolute;left:10px;width:780px;overflow:hidden;border:1px solid var(--page-edge);
  background:linear-gradient(170deg,var(--page-top),var(--page-bottom))}
.page--front{top:47px;height:553px}
.page--back{top:628px;height:553px}
.brand{position:absolute;left:50%;transform:translateX(-50%);border-radius:50%;background:var(--panel);
  display:flex;align-items:center;justify-content:center;text-align:center;color:var(--ink-soft);
  font-weight:400;letter-spacing:1px;line-height:1.15}
.page--front .brand{top:10px;width:84px;height:84px;font-size:11px}
.page--back .brand{top:8px;width:60px;height:60px;font-size:8px}
.masthead{position:absolute;left:0;right:0;text-align:center}
.masthead h1{font-weight:400;letter-spacing:.5px}
.masthead p{font-style:italic}
.page--front .masthead{top:107px}
.page--front .masthead h1{font-size:15px}
.page--front .masthead p{font-size:10px}
.page--back .masthead{top:72px}
.page--back .masthead h1{font-size:11px}
.page--back .masthead p{font-size:10px;margin-top:-1px}
.panel{position:absolute;background:var(--panel);border:1.5px solid var(--panel-line)}
.ribbon{position:absolute;display:flex;align-items:center;justify-content:center}
.ribbon svg{position:absolute;inset:0;width:100%;height:100%}
.ribbon span{position:relative;font-weight:400;text-align:center;line-height:1.1;letter-spacing:.5px}
.price-list{list-style:none;font-size:10px}
.price-list li{display:flex;justify-content:space-between;height:16.8px;align-items:center}
.note{font-size:7.5px;font-style:italic;margin-top:14px;line-height:2.1}
.photo{position:absolute;border-radius:50%}
.lunch-text{font-size:7.6px;line-height:11.2px;padding:26px 10px 0 10px}
.lunch-text b{font-weight:600}
.lunch-text i{color:var(--ink-soft)}
.lunch-text .gap{height:11px}
</style>
</head>
<body>

<section class="page page--front">
  <div class="brand">BEDSIDE<br>CAFE</div>
  <header class="masthead">
    <h1>CATERING MENU</h1>
    <p>Visit us instore to discuss catering options or call 0438 672 914 or email marla@tevrostudio.com.au</p>
  </header>

  <div class="panel" style="left:30px;top:168px;width:331px;height:274px">
    <ul class="price-list" style="padding:42px 22px 0 20px">
      <li><span>Fruit Platter</span><span>$15</span></li>
      <li><span>Bacon Egg and Cheese Roll</span><span>$6.5</span></li>
      <li><span>Vegetarian Brekky Wrap</span><span>$6.5</span></li>
      <li><span>Ham and Cheese Croissant</span><span>$6</span></li>
      <li><span>Cheese and Tomato Croissant</span><span>$5.5</span></li>
      <li><span>Ham and Cheese French Toast</span><span>$6.5</span></li>
      <li><span>Assorted Yoghurts</span><span>$5.5</span></li>
      <li><span>Bircher Muesli</span><span>$5.5</span></li>
      <li><span>Chia Pudding</span><span>$5.5</span></li>
      <li><span>Granola and Yoghurt</span><span>$5.5</span></li>
      <li><span>Muffin</span><span>$4.5</span></li>
      <li><span>Mini Muffin</span><span>$2.5</span></li>
      <li><span>Juice</span><span>$8</span></li>
    </ul>
  </div>
  <div class="ribbon" style="left:130px;top:148px;width:135px;height:40px">
    <svg viewBox="0 0 135 40" preserveAspectRatio="none"><polygon points="1,1 134,1 122,20 134,39 1,39 13,20" fill="var(--panel)" stroke="var(--panel-line)" stroke-width="1.5"/></svg>
    <span style="font-size:12px">HOT BEVERAGE</span>
  </div>

  <div class="panel" style="left:422px;top:168px;width:331px;height:274px">
    <ul class="price-list" style="padding:42px 22px 0 27px">
      <li><span>Fruit Platter</span><span>$15</span></li>
      <li><span>Muffin</span><span>$4.5</span></li>
      <li><span>Mini Muffin</span><span>$2.5</span></li>
      <li><span>Assorted Slices</span><span>$4</span></li>
      <li><span>Assorted Cookies from</span><span>$3</span></li>
      <li><span>Assorted Yoghurts</span><span>$5.5</span></li>
      <li><span>Chia Pudding</span><span>$5.5</span></li>
      <li><span>Banana Bread</span><span>$4.5</span></li>
      <li><span>Juice</span><span>$8</span></li>
    </ul>
    <p class="note" style="padding-left:27px">*Cups/Plates/Serviettes can be provided at a charge of $1 per person<br>*Barista made coffee available</p>
  </div>
  <div class="ribbon" style="left:518px;top:148px;width:135px;height:40px">
    <svg viewBox="0 0 135 40" preserveAspectRatio="none"><polygon points="1,1 134,1 122,20 134,39 1,39 13,20" fill="var(--panel)" stroke="var(--panel-line)" stroke-width="1.5"/></svg>
    <span style="font-size:11px">MORNING AND<br>AFTERNOON TEA</span>
  </div>

  <div class="photo" role="img" aria-label="Cups of tea" style="left:-15px;top:443px;width:110px;height:110px;background:radial-gradient(circle at 40% 40%,#c9364a,#4a3a8a 70%,#e8e0ea)"></div>
  <div class="photo" role="img" aria-label="Potato wedges" style="left:115px;top:443px;width:121px;height:121px;background:radial-gradient(circle,#d99a4a,#8a4f22)"></div>
  <div class="photo" role="img" aria-label="Chicken wings with dip" style="left:250px;top:443px;width:121px;height:121px;background:radial-gradient(circle at 50% 40%,#e6e3dc 15%,#c23a2a 45%,#7a1e18)"></div>
  <div class="photo" role="img" aria-label="Sandwich and grapes" style="left:410px;top:443px;width:121px;height:121px;background:radial-gradient(circle,#c9b08a,#6f5a43 80%)"></div>
  <div class="photo" role="img" aria-label="Pizza slices" style="left:545px;top:443px;width:121px;height:121px;background:radial-gradient(circle,#d46a4a,#8a3a2a)"></div>
  <div class="photo" role="img" aria-label="Spinach wraps" style="left:677px;top:450px;width:121px;height:121px;background:radial-gradient(circle,#8fae3a,#3f6a22)"></div>
</section>

<section class="page page--back">
  <div class="photo" role="img" aria-label="Soft peach bokeh light" style="left:-40px;top:-30px;width:120px;height:120px;background:radial-gradient(circle,var(--cream),var(--peach))"></div>
  <div class="photo" role="img" aria-label="Soft peach bokeh light" style="left:668px;top:-12px;width:130px;height:130px;background:radial-gradient(circle,var(--cream),var(--peach))"></div>
  <div role="img" aria-label="Fresh salad bowl" style="position:absolute;left:250px;top:130px;width:360px;height:430px;border-radius:40% 40% 0 0;background:radial-gradient(ellipse at 50% 60%,#8aa35a,#b8472e 45%,#5a4a3f 75%);opacity:.55"></div>

  <div class="brand">BEDSIDE<br>CAFE</div>
  <header class="masthead">
    <h1>CATERING MENU</h1>
    <p>Visit us instore to discuss catering options or call 0438 672 914 or email marla@tevrostudio.com.au</p>
  </header>

  <div class="panel" style="left:30px;top:122px;width:331px;height:414px;background:rgba(45,36,48,.92)">
    <div class="lunch-text">
      <b>Sandwiches  or Wraps $7.50</b> <i>Sandwiches cut into quarters – Wraps cut into thirds</i><br>
      <b>Ham:</b> <i>butter, pickle spread, cheese, tomato, champagne leg ham</i><br>
      <b>Turkey:</b> <i>butter, cranberry sauce, lettuce mix, tomato, turkey breast</i><br>
      <b>Sweet Chilli Chicken:</b> <i>butter, sweet chilli sauce, aioli, lettuce mix, tomato, cheese, sweet chilli chicken tenders</i><br>
      <b>Chicken Schnitzel:</b> <i>butter, aioli, lettuce mix, tomato, tasty cheese, chicken schnitzel</i><br>
      <b>Chicken and Avocado:</b> <i>butter, aioli, lettuce mix, tomato, cheese, chicken breast, avocado</i><br>
      <b>Egg:</b> <i>butter, lettuce mix, egg, aioli, parsley, spring onion</i><br>
      <b>Tuna:</b> <i>butter, lettuce, tuna, aioli, sundried tomato, spring onion</i><br>
      <b>B.L.T.:</b> <i>butter, aioli, lettuce, tomato, bacon</i><br>
      <b>Salad:</b> <i>butter, lettuce mix, red onion, cucumber, capsicum, tomato, avocado, tasty cheese</i><br>
      <b>Tandoori Chicken:</b> <i>butter, tzatziki, lettuce mix, tomato, tandoori chicken</i><br>
      <b>Waldorf Chicken:</b> <i>butter, cos lettuce, chicken, seeded mustard, celery, walnuts, aioli</i><br>
      <b>Chicken Ceasar:</b> <i>butter, aioli, cos lettuce, chicken, parmesan cheese, bacon</i><br>
      <b>Cajun Chicken:</b> <i>butter, lettuce mix, tomato, red onion, Cajun chicken</i><br>
      <b>-Barbeque Chicken: butter, BBQ,</b><br>
      <b>-Felafel:</b>
      <div class="gap"></div>
      <b>Foccacias $8.50</b><br>
      <i>Cut in half – please let us know if you want them toasted</i><br>
      <i>**Same options as wraps and sandwiches – Plus:</i><br>
      <b>Roast Veggie:</b> <i>butter, pesto, grilled eggplant, grilled zucchini, roasted capsicum, feta cheese, baby spinach</i><br>
      <b>Salami:</b> <i>butter, pesto, baby spinach, mild salami, roasted capsicum, olives, feta cheese</i><br>
      <b>Chicken Schnitzel:</b> <i>Butter, Housemade coleslaw, chicken schnitzel</i>
      <div class="gap"></div>
      <b>Bagels $9.0</b><br>
      <b>Turkey:</b> <i>butter, cranberry sauce, baby spinach, tomato, camembert cheese</i><br>
      <b>Smoked Salmon:</b> <i>butter, cream cheese, baby spinach, tomato, smoked salmon</i>
    </div>
  </div>
  <div class="ribbon" style="left:133px;top:102px;width:130px;height:40px">
    <svg viewBox="0 0 130 40" preserveAspectRatio="none"><polygon points="1,1 129,1 117,20 129,39 1,39 13,20" fill="var(--panel)" stroke="var(--panel-line)" stroke-width="1.5"/></svg>
    <span style="font-size:17px">LUNCH</span>
  </div>

  <div class="panel" style="left:422px;top:169px;width:331px;height:274px;background:rgba(45,36,48,.92)">
    <ul class="price-list" style="padding:31px 28px 0 27px">
      <li><span>Assorted Pies</span><span>$5.0</span></li>
      <li><span>Large tray hot chips</span><span>$15</span></li>
      <li><span>Small tray hot chips</span><span>$9</span></li>
      <li><span>Mini samosa</span><span>$3</span></li>
      <li><span>Vegetarian spring rolls</span><span>$3</span></li>
      <li><span>Party pies</span><span>$3</span></li>
      <li><span>Mini sausage rolls</span><span>$3</span></li>
      <li><span>Mini quiche</span><span>$3</span></li>
      <li><span>Mini dim sim</span><span>$2</span></li>
      <li><span>Sweet chilli chicken tenders</span><span>$3</span></li>
      <li><span>Meatballs</span><span>$2</span></li>
      <li><span>Spinach and ricotta pastizi</span><span>$3</span></li>
      <li><span>Vegetarian Frittata</span><span>$4.5</span></li>
      <li><span>Meat Frittata</span><span>$4.5</span></li>
    </ul>
  </div>
  <div class="ribbon" style="left:522px;top:149px;width:130px;height:40px">
    <svg viewBox="0 0 130 40" preserveAspectRatio="none"><polygon points="1,1 129,1 117,20 129,39 1,39 13,20" fill="var(--panel)" stroke="var(--panel-line)" stroke-width="1.5"/></svg>
    <span style="font-size:16px">HOT FOOD</span>
  </div>
</section>

</body>
</html>
```